New Wordpress Design Project

The website is my name tessamaybrook.com

I need a website design that will be graphically pleasing and have a crisp feel to it. I am a business and personal coach and have many different niches that I work with. I am looking for the central site to describe who I am and how I help people - I help people "wake up" to make conscious choices in their lives. I use hypnosis but do not want it to be esoteric, I ground the hypnosis and base it in science of how people can manage their state to reach their full potential in their lives and in business. I work one on one but also do public speaking and recently started to do trainings with corporations, helping people improve their business. I am looking at this as a merge of hypnosis and other tools with the business or corporate world - based in science - neuroplasticity, brain training etc. I will be helping people to overcome anxiety and stress, limiting beliefs, controlling and choosing habits that will work for them, fears and phobias, golf/sports improvement, weight loss.

Really helping people to center back with themselves, to not be so caught up in their head but drop into their heart and with what is really going on. My mission is to connect them back with themselves, using language, state and conscious choice.

I work online with entrepreneurs helping them to get unstuck, move past fears and limiting beliefs to create the business of their dreams.

I added a file of what I am envisioning on the right hand side of my site to show people the different niches I am involved with.

Some sites that I like www.gretavanholt.com www.corinnemaddox.org http://www.judekestrel.com/ , Details for my new Wordpress Design Project will be added soon. , The website is my name tessamaybrook.com

the square boxes graphic below is similar to one that I will be making for a page on my site for clarity and crispness. But will be creating it more in the teal color.

Target Market(s)

My target market are both male and female 30-50 either entreprenuers/business people

Industry/Entity Type

Training

Requirements
Must have
• A video with an opt in box
My background color is teal/blue (see below file)
Social media links

```html
<!DOCTYPE html>
<html lang="en">
<head>
<meta charset="utf-8">
<title>TessaMayBrook – Optimizing Your Mindset for Entrepreneurial Success</title>
<link href="https://fonts.googleapis.com/css2?family=Lobster&family=Open+Sans:ital,wght@0,400;0,600;0,700;1,400&display=swap" rel="stylesheet">
<style>
  :root {
    --backdrop: #4b4b4b;
    --teal-strip: #0f8f97;
    --teal-header: #16b3bb;
    --teal-hero: #13a0a6;
    --teal-hero-dark: #0c858b;
    --teal-deep: #2b6c74;
    --teal-link: #1aa9b4;
    --field: #c3f0f2;
    --field-text: #3aa9b0;
    --yellow: #f2e53c;
    --yellow-dark: #d9c820;
    --grey-bar: #d6d8d8;
    --dot: #a9abab;
    --text: #8a8a8a;
    --heading: #2f2f2f;
    --white: #ffffff;
    --rule: #cfcfcf;
  }
  * { box-sizing: border-box; margin: 0; padding: 0; }
  html, body { width: 1200px; height: 1000px; overflow: hidden; }
  body { background: var(--backdrop); font-family: "Open Sans", sans-serif; position: relative; }
  .page { position: absolute; left: 43px; top: 43px; width: 1114px; height: 1000px; background: var(--white); overflow: hidden; box-shadow: 0 0 8px rgba(0,0,0,.4); }
  .abs { position: absolute; }

  .top-strip { left: 0; top: 0; width: 100%; height: 25px; background: var(--teal-strip); }
  .site-header { left: 0; top: 25px; width: 100%; height: 73px; background: linear-gradient(180deg, #1bbcc4, var(--teal-header)); border-bottom: 2px solid #5fd0d5; }
  .brand-dot { left: 150px; top: 37px; width: 48px; height: 48px; border-radius: 50%; background: #5fcfd5; }
  .brand-name { left: 210px; top: 34px; font-weight: 700; font-size: 30px; letter-spacing: 2px; color: var(--teal-deep); }
  .brand-tagline { left: 211px; top: 73px; font-size: 11px; color: var(--teal-deep); }
  .main-nav { left: 576px; top: 56px; display: flex; font-size: 11.5px; color: #2c7f86; }
  .main-nav a { color: inherit; text-decoration: none; margin-right: 0; }
  .main-nav a.current { color: var(--white); }
  .main-nav .n1 { width: 71px; } .main-nav .n2 { width: 62px; } .main-nav .n3 { width: 85px; } .main-nav .n4 { width: 90px; }

  .hero { left: 0; top: 100px; width: 100%; height: 367px; background: radial-gradient(ellipse at 55% 40%, #1eb3b9, var(--teal-hero) 45%, var(--teal-hero-dark)); }
  .slide-arrow { top: 169px; width: 26px; height: 26px; border-radius: 50%; background: #0f8990; }
  .slide-arrow svg { display: block; }
  .video { left: 154px; top: 62px; width: 394px; height: 240px; background: linear-gradient(135deg, #3d5a2a, #8ca35a 45%, #c9b07a 60%, #556b3a); box-shadow: 0 8px 10px rgba(0,0,0,.35); }
  .play { left: 166px; top: 89px; width: 62px; height: 62px; border-radius: 50%; background: rgba(255,255,255,.4); }
  .video-caption { left: 0; bottom: 0; width: 100%; height: 34px; background: rgba(40,40,40,.6); color: var(--white); font-size: 11.5px; padding: 10px 20px; }
  .optin-title { left: 590px; top: 52px; font-family: "Lobster", cursive; font-size: 32px; color: var(--white); }
  .optin-text { left: 591px; top: 100px; width: 380px; font-size: 11.5px; line-height: 20.5px; color: var(--white); }
  .field { left: 591px; width: 315px; height: 30px; background: var(--field); font-size: 11.5px; color: var(--field-text); padding: 7px 10px; }
  .submit { left: 591px; top: 275px; width: 105px; height: 30px; background: linear-gradient(180deg, var(--yellow), var(--yellow-dark)); font-size: 11px; font-weight: 700; color: #6a6320; text-align: center; line-height: 30px; }

  .pager { left: 0; top: 464px; width: 100%; height: 45px; background: var(--grey-bar); }
  .pager span { position: absolute; top: 18px; width: 12px; height: 12px; border-radius: 50%; background: var(--dot); box-shadow: inset 0 1px 2px rgba(0,0,0,.2); }

  .post-title { left: 154px; font-family: "Lobster", cursive; font-size: 20px; color: var(--heading); }
  .post-meta { left: 154px; font-size: 11px; font-style: italic; color: var(--text); display: flex; align-items: center; gap: 4px; }
  .post-meta a { color: var(--teal-link); text-decoration: none; }
  .dash { left: 154px; width: 506px; border-top: 1px dashed var(--rule); }
  .thumb-frame { left: 154px; width: 154px; height: 155px; border: 1px solid #d5d5d5; padding: 6px; background: var(--white); }
  .thumb { width: 100%; height: 100%; }
  .excerpt { left: 324px; width: 340px; font-size: 11.5px; line-height: 20.5px; color: var(--text); }
  .post-tax { left: 154px; font-size: 11px; font-style: italic; color: var(--text); line-height: 14px; }
  .post-tax a { color: var(--teal-link); text-decoration: none; }
  .read-more { left: 575px; width: 85px; height: 24px; border: 1px solid #cfcfcf; border-radius: 3px; background: linear-gradient(#f0f0f0, #dcdcdc); font-size: 11px; color: #888; text-align: center; line-height: 22px; }

  .promo { left: 729px; width: 231px; height: 76px; border-radius: 3px; box-shadow: 0 6px 6px rgba(0,0,0,.25); color: var(--white); text-align: center; font-weight: 700; }
  .promo .big { display: block; font-size: 17px; letter-spacing: 4px; margin-top: 23px; line-height: 20px; }
  .promo .small { display: block; font-size: 9.5px; letter-spacing: 5px; }
  .promo-fear { top: 584px; background: linear-gradient(90deg, #a8404a, #e06068 50%, #c44b55); }
  .promo-time { top: 680px; background: linear-gradient(90deg, #1d1d10, #3e3d14 50%, #24240f); }
  .promo-interview { top: 779px; background: linear-gradient(90deg, #0e3a12, #2c8a2e 50%, #155a18); }
  .promo-time .big { letter-spacing: 1px; font-size: 19px; }

  .about-box { left: 728px; top: 900px; width: 232px; height: 140px; border: 1px solid #dcdcdc; border-radius: 4px; background: #f4f4f4; }
  .about-title { left: 20px; top: 18px; font-family: "Lobster", cursive; font-size: 20px; color: var(--heading); }
  .about-rule { left: 20px; top: 52px; width: 190px; border-top: 1px solid #d0d0d0; }
</style>
</head>
<body>
<div class="page">
  <div class="abs top-strip"></div>

  <header class="abs site-header">
    <div class="abs brand-dot" style="top:12px;left:150px"></div>
    <div class="abs brand-name" style="top:9px">TessaMayBrook</div>
    <div class="abs brand-tagline" style="top:48px">Optimizing Your Mindset for Entrepreneurial Success</div>
    <nav class="abs main-nav" style="top:31px">
      <a class="n1 current" href="#">Home »</a>
      <a class="n2" href="#">Blog »</a>
      <a class="n3" href="#">About Me »</a>
      <a class="n4" href="#">Contact Me »</a>
      <a href="#">List of Books »</a>
    </nav>
  </header>

  <section class="abs hero">
    <div class="abs slide-arrow" style="left:84px"><svg width="26" height="26" viewBox="0 0 26 26"><path d="M15 7 L9 13 L15 19" fill="none" stroke="#2bd0d8" stroke-width="3"/></svg></div>
    <div class="abs slide-arrow" style="left:1002px"><svg width="26" height="26" viewBox="0 0 26 26"><path d="M11 7 L17 13 L11 19" fill="none" stroke="#2bd0d8" stroke-width="3"/></svg></div>

    <div class="abs video" role="img" aria-label="Introductory video still of the coach seated outdoors in green foliage">
      <div class="abs play"><svg width="62" height="62" viewBox="0 0 62 62"><path d="M25 19 L43 31 L25 43 Z" fill="rgba(80,80,80,.75)"/></svg></div>
      <div class="abs video-caption">Lorem ipsum dolor sit amet, consecteru adsipcing elit...</div>
    </div>

    <h1 class="abs optin-title">Lorem ipsum dolor sit amet...</h1>
    <p class="abs optin-text">Lorem ipsum dolor sit amet, consectetur adipisicing elit, sed do eiusmod tempor incididunt ut labore et dolor. Ut enim ad minim en iam, quis nostrud exercitation ullamco laboris...</p>
    <div class="abs field" style="top:179px">Your Name</div>
    <div class="abs field" style="top:226px">Email Address</div>
    <div class="abs submit">Submit</div>
  </section>

  <div class="abs pager">
    <span style="left:486px;background:#949696"></span><span style="left:512px"></span><span style="left:537px"></span>
  </div>

  <!-- Post one -->
  <h2 class="abs post-title" style="top:578px">Ut rutrum tortor in scelerisque mollis.</h2>
  <div class="abs post-meta" style="top:610px">✎ Written by <a href="#">TESSA MAY</a> on <a href="#">December 7, 2012</a> | 💬 <a href="#">436 comments</a></div>
  <div class="abs dash" style="top:629px"></div>
  <div class="abs thumb-frame" style="top:647px"><div class="thumb" role="img" aria-label="Colourful painted artwork for the post" style="background:linear-gradient(135deg,#4fb8c0,#9ad0c8 40%,#e07a3a 70%,#c23a2a)"></div></div>
  <p class="abs excerpt" style="top:642px">Duis aute irure dolor in reprehenderit in voluptate velit esse cillum dolore eu fugiat nulla pariatur. Excepteur sint occaecat cupidatat non proident, sunt in culpa qui officia deserunt mollit anim id est laborum. Sed ut perspiciatis unde omnis iste natus error sit voluptatem accusantium doloremque laudantium, totam rem aperiam, eaque ipsa quae ab illo inventore veritatis et quasi architecto beatae vitae dicta sunt explicabo. Nemo enim ipsam voluptatem quia voluptas sit aspernatur aut odit aut fugit,</p>
  <div class="abs post-tax" style="top:817px">Categories: <a href="#">Limiting Beliefs</a><br>Tags: <a href="#">beliefs</a>, <a href="#">change</a>, <a href="#">desire</a>, <a href="#">money</a>.</div>
  <div class="abs read-more" style="top:821px">Read More</div>

  <!-- Post two -->
  <h2 class="abs post-title" style="top:871px">Vivamus ut dui eget sem bibendum consectetur</h2>
  <div class="abs post-meta" style="top:904px">✎ Written by <a href="#">TESSA MAY</a> on <a href="#">December 7, 2012</a> | 💬 <a href="#">436 comments</a></div>
  <div class="abs dash" style="top:923px"></div>
  <div class="abs thumb-frame" style="top:946px"><div class="thumb" role="img" aria-label="Photograph for the post" style="background:linear-gradient(135deg,#e8e6d8,#b8b490)"></div></div>
  <p class="abs excerpt" style="top:941px">Sed ut perspiciatis unde omnis iste natus error sit voluptatem</p>

  <!-- Sidebar -->
  <a class="abs promo promo-fear" href="#" role="img" aria-label="Overcome fear and self doubt banner"><span class="big">OVERCOME</span><span class="small">FEAR + SELF DOUBT</span></a>
  <a class="abs promo promo-time" href="#" role="img" aria-label="Get more done in less time banner"><span class="big">GET <span style="font-family:'Lobster',cursive;font-weight:400;letter-spacing:0">More</span> DONE</span><span class="small">IN LESS TIME</span></a>
  <a class="abs promo promo-interview" href="#" role="img" aria-label="My Halloway interview banner"><span class="big">MY HALLOWAY</span><span class="small">INTERVIEW</span></a>

  <aside class="abs about-box">
    <h3 class="abs about-title">About Tessa May...</h3>
    <div class="abs about-rule"></div>
  </aside>
</div>
</body>
</html>
```